Looking for a modern, Professional business card design

We have a simple business card, but are looking for a more modern, professional look. A sample of the basic card is attached as well as the logo. We would also like to add that we offer:
Struggling with your finances?
- Learn to become debt free
- Discover the power of cash
- Control your money instead of it controlling you
Let us help you achieve a new level of financial freedom!
Also, we would like to have a "SPECIAL OFFER!: FREE 30 minute consultation"
Financial Planning

```html
<!DOCTYPE html>
<html lang="en">
<head>
<meta charset="utf-8">
<title>Keelwise – Business Card</title>
<link href="https://fonts.googleapis.com/css2?family=Russo+One&family=Open+Sans:ital,wght@0,400;0,600;0,700;1,400;1,600&display=swap" rel="stylesheet">
<style>
  :root {
    --page-bg: #ecebe8;
    --card-white: #ffffff;
    --ink: #1b1b1b;
    --panel-black: #1f1f1f;
    --green-dark: #1f9a3c;
    --green-mid: #5cb82e;
    --green-light: #9fd13a;
    --muted: #555555;
  }
  * { margin: 0; padding: 0; box-sizing: border-box; }
  html, body { width: 1200px; height: 900px; overflow: hidden; }
  body {
    background: var(--page-bg);
    font-family: "Open Sans", Arial, sans-serif;
    position: relative;
  }
  .card {
    position: absolute;
    left: 300px;
    width: 600px;
    height: 343px;
    background: var(--card-white);
    border-radius: 18px;
    overflow: hidden;
    box-shadow: 0 6px 18px rgba(0,0,0,0.18);
  }
  .card--front { top: 80px; }
  .card--back { top: 477px; }
  .card__art { position: absolute; inset: 0; width: 600px; height: 343px; }

  .wordmark {
    font-family: "Open Sans", Arial, sans-serif;
    font-weight: 700;
    color: var(--ink);
    line-height: 1;
  }

  /* front */
  .front__brand { position: absolute; left: 298px; top: 50px; font-size: 40px; }
  .front__person { position: absolute; left: 298px; top: 152px; }
  .person__name {
    font-family: "Russo One", Arial, sans-serif;
    font-size: 25px; color: var(--ink); text-transform: uppercase;
  }
  .person__title {
    font-family: "Russo One", Arial, sans-serif;
    font-size: 13px; color: var(--green-dark); text-transform: uppercase; margin-top: 2px;
  }
  .contact { list-style: none; position: absolute; left: 298px; top: 226px; font-size: 14px; color: var(--ink); }
  .contact li { display: flex; align-items: center; gap: 8px; line-height: 24px; }
  .contact svg { width: 14px; height: 14px; flex: none; }

  /* back */
  .pitch { position: absolute; left: 30px; top: 30px; width: 320px; color: #fff; }
  .pitch__headline { font-size: 17px; font-style: italic; font-weight: 600; color: var(--green-light); margin-bottom: 8px; }
  .pitch__list { list-style: none; font-size: 12.5px; line-height: 20px; }
  .pitch__list li { display: flex; align-items: center; gap: 7px; }
  .pitch__list svg { width: 11px; height: 11px; flex: none; }
  .pitch__close { font-size: 12.5px; font-style: italic; margin-top: 6px; line-height: 18px; }
  .offer__title {
    font-family: "Russo One", Arial, sans-serif;
    font-size: 30px; color: var(--green-light); margin-top: 18px; text-transform: uppercase;
  }
  .offer__detail { font-size: 16px; font-weight: 700; text-transform: uppercase; letter-spacing: 0.5px; }
  .back__brand { position: absolute; left: 440px; top: 152px; font-size: 32px; }
</style>
</head>
<body>

<section class="card card--front" aria-label="Card front">
  <svg class="card__art" viewBox="0 0 600 343" aria-hidden="true">
    <path d="M0 0 H150 C235 95 262 230 240 343 H0 Z" fill="var(--green-light)"/>
    <path d="M0 0 H138 C222 95 248 230 226 343 H0 Z" fill="var(--green-dark)"/>
    <path d="M0 0 H126 C208 95 232 230 210 343 H0 Z" fill="var(--panel-black)"/>
  </svg>
  <p class="wordmark front__brand">Keelwise</p>
  <div class="front__person">
    <p class="person__name">Daniel R. Hayes</p>
    <p class="person__title">Personal Financial Coach</p>
  </div>
  <ul class="contact">
    <li><svg viewBox="0 0 14 14"><path d="M3 1h3l1 3-2 1a8 8 0 0 0 4 4l1-2 3 1v3a1 1 0 0 1-1 1A11 11 0 0 1 2 2a1 1 0 0 1 1-1z" fill="var(--green-dark)"/></svg>(205) 555-0187</li>
    <li><svg viewBox="0 0 14 14"><rect x="1" y="3" width="12" height="8" fill="none" stroke="var(--green-dark)" stroke-width="1.5"/><path d="M1 3l6 5 6-5" fill="none" stroke="var(--green-dark)" stroke-width="1.5"/></svg>daniel@steadymoneypath.com</li>
    <li><svg viewBox="0 0 14 14"><circle cx="7" cy="7" r="6" fill="none" stroke="var(--green-dark)" stroke-width="1.5"/><path d="M1 7h12M7 1c3 3 3 9 0 12M7 1c-3 3-3 9 0 12" fill="none" stroke="var(--green-dark)" stroke-width="1.2"/></svg>www.steadymoneypath.com</li>
  </ul>
</section>

<section class="card card--back" aria-label="Card back">
  <svg class="card__art" viewBox="0 0 600 343" aria-hidden="true">
    <path d="M0 0 H370 C440 90 440 260 370 343 H0 Z" fill="var(--green-dark)"/>
    <path d="M0 0 H360 C426 90 426 260 360 343 H0 Z" fill="var(--green-light)"/>
    <path d="M0 0 H350 C412 90 412 260 350 343 H0 Z" fill="var(--panel-black)"/>
  </svg>
  <div class="pitch">
    <p class="pitch__headline">Struggling with your finances?</p>
    <ul class="pitch__list">
      <li><svg viewBox="0 0 11 11"><path d="M1 4h5V1l4 4.5L6 10V7H1z" fill="var(--green-light)"/></svg>Learn to become debt free</li>
      <li><svg viewBox="0 0 11 11"><path d="M1 4h5V1l4 4.5L6 10V7H1z" fill="var(--green-light)"/></svg>Discover the power of cash</li>
      <li><svg viewBox="0 0 11 11"><path d="M1 4h5V1l4 4.5L6 10V7H1z" fill="var(--green-light)"/></svg>Control your money instead of it controlling you</li>
    </ul>
    <p class="pitch__close">Let us help you achieve a new level of financial freedom!</p>
    <p class="offer__title">Special Offer!</p>
    <p class="offer__detail">Free 30 Minute Consultation</p>
  </div>
  <p class="wordmark back__brand">Keelwise</p>
</section>

</body>
</html>
```